Restaurant needs take out menu design

I need a takeout menu design for a new restaurant. We will be printing via inkharbor.com. On their website, you can download blank templates.

See specs:
1. 11x17 accordion folding. http://www.inkharbor.com/take-out-menu-printing.html
2. Font is Times New Roman
3. All design/font on the menu will be black

*See menu inspiration attached. Feel free to reuse similar boarders and design.
*Attached is our logo
*Please let me know if any other information is needed.
*Attached is a our menu with prices.
*Please send to me in an ai file.

Industry/Entity Type

Restaurant

Font styles to use
Serif
Decorative

Requirements
Must have
• new times roman. black lettering
• all uppercase lettering
• must be in adobe illustrator format
• have the same feel as the menus I attached
Nice to have
• Leave the area for the telephone numbers, hours, address and business hours the same as the copy and pasted menu.
Should not have
• No other color than black

```html
<!DOCTYPE html>
<html lang="en">
<head>
<meta charset="utf-8">
<title>The Jade Hall – Take Out Menu</title>
<link href="https://fonts.googleapis.com/css2?family=Tinos:ital,wght@0,400;0,700;1,400&family=Arimo:ital@1&display=swap" rel="stylesheet">
<style>
  :root{
    --ink:#0d0d0d;
    --paper:#ffffff;
    --ornament:#dcdcdc;
    --row:19.2px;
  }
  *{box-sizing:border-box;margin:0;padding:0}
  html,body{width:1200px;height:1200px;overflow:hidden;background:var(--paper)}
  body{position:relative;font-family:"Tinos","Times New Roman",serif;color:var(--ink);text-transform:uppercase}

  .panel{position:absolute;top:18px;width:389px;height:1164px;background:var(--ink);border-radius:22px}
  .panel--left{left:14px}
  .panel--middle{left:406px}
  .panel--right{left:797px}
  .panel__inner{position:absolute;inset:12px 11px;background:var(--paper);border-radius:14px}

  .corner{position:absolute;width:34px;height:30px;background:var(--ornament);border-radius:6px}
  .corner--tl{top:30px;left:20px}.corner--tr{top:30px;right:20px}
  .corner--bl{bottom:32px;left:20px}.corner--br{bottom:32px;right:20px}

  .block{position:absolute;left:0;right:0}
  .heading{text-align:center;font-size:27px;line-height:30px;font-weight:400;letter-spacing:.3px}
  .heading span{border-bottom:2px solid var(--ink);padding:0 2px 1px}

  .list{position:absolute;left:0;right:0;font-size:11.6px;letter-spacing:-.15px}
  .row{position:relative;height:var(--row);line-height:var(--row);padding-left:31px;white-space:nowrap}
  .price{position:absolute;top:0}
  .note{font-style:italic;font-size:10.4px}

  .panel--left .row{padding-left:31px}
  .panel--left .price{left:298px}
  .panel--left .price--qt{left:327px}
  .col-head{position:absolute;top:96px;font-size:12px}

  .brand{position:absolute;top:62px;left:0;right:0;text-align:center;font-weight:400;line-height:1}
  .brand__the{display:block;font-size:26px;letter-spacing:14px;padding-left:14px}
  .brand__name{display:block;font-size:52px;margin-top:10px;letter-spacing:1px}

  .panel--middle .price{left:296px}
  .fish{position:absolute;left:31px;right:14px;font-size:11.6px}
  .fish__name{position:relative;line-height:18px;white-space:nowrap}
  .fish__mp{position:absolute;left:238px;top:0;font-size:10px;font-weight:700;white-space:nowrap}
  .fish__desc{font-style:italic;font-size:10.4px;line-height:17.6px;width:270px}
  .address{position:absolute;top:1110px;left:0;right:0;text-align:center;font-family:"Arimo",Arial,sans-serif;font-style:italic;font-size:13.5px;text-transform:none}

  .panel--right .price{left:322px}
  .special{position:absolute;left:31px;right:12px;font-size:11.6px}
  .special__name{position:relative;line-height:var(--row)}
  .special__name .price{left:291px}
  .special__desc{font-style:italic;font-size:11.6px;line-height:var(--row)}
  .divider{position:absolute;top:972px;left:120px;width:130px;height:18px;background:var(--ornament);border-radius:9px}
  .footnote{position:absolute;top:998px;left:0;right:0;text-align:center;font-size:11px;line-height:15.6px}
  .call{position:absolute;top:1094px;left:0;right:0;text-align:center;font-style:italic;font-size:17px}
</style>
</head>
<body>

<section class="panel panel--left">
  <div class="panel__inner">
    <span class="corner corner--tl" role="img" aria-label="corner flourish"></span>
    <span class="corner corner--tr" role="img" aria-label="corner flourish"></span>
    <span class="corner corner--bl" role="img" aria-label="corner flourish"></span>
    <span class="corner corner--br" role="img" aria-label="corner flourish"></span>

    <h2 class="block heading" style="top:64px;left:-30px"><span>Soups</span></h2>
    <span class="col-head" style="left:300px">Pt.</span>
    <span class="col-head" style="left:330px">Qt.</span>
    <div class="list" style="top:116px">
      <div class="row">Egg Drop Soup<span class="price">2.75</span><span class="price price--qt">4.95</span></div>
      <div class="row">Hot &amp; Sour Soup<span class="price">3.95</span><span class="price price--qt">6.75</span></div>
      <div class="row">Wonton Soup<span class="price">3.95</span><span class="price price--qt">6.75</span></div>
      <div class="row">Bean Curd Soup With</div>
      <div class="row">Vegetables (2)<span class="price">6.95</span></div>
      <div class="row">Chicken Corn Soup (2)<span class="price">7.95</span></div>
      <div class="row">Ten Ingredients Rice Soup (2)<span class="price">7.95</span></div>
      <div class="row">Symphony Seafood Soup (For 2)<span class="price">2.95</span></div>
    </div>

    <h2 class="block heading" style="top:270px;left:-30px"><span>Appetizers</span></h2>
    <div class="list" style="top:320px">
      <div class="row">Vegetable Roll<span class="price">2.25</span></div>
      <div class="row">Egg Roll<span class="price">2.50</span></div>
      <div class="row">Shrimp Roll<span class="price">2.50</span></div>
      <div class="row">Steamed Edamame<span class="price">3.95</span></div>
      <div class="row">Scallion Pancakes<span class="price">4.50</span></div>
      <div class="row">Cold Noodles in Sesame Sauce<span class="price">4.95</span></div>
      <div class="row">Crispy Crab Ragoon (3)<span class="price">4.95</span></div>
      <div class="row">Shrimp Toast (4)<span class="price">5.75</span></div>
      <div class="row">Barbecued Beef Sticks (2)<span class="price">5.95</span></div>
      <div class="row">Steamed Dumplings (6)<span class="price">6.50</span></div>
      <div class="row">Pan Fried Dumplings (6)<span class="price">6.50</span></div>
      <div class="row">Dumplings With Hot Oil (Peanut</div>
      <div class="row">Sesame Sauce) (6)<span class="price">6.50</span></div>
      <div class="row">&nbsp;Spicy Chicken Dumplings (10)<span class="price">6.50</span></div>
      <div class="row">Steamed Edamame</div>
      <div class="row">Dumplings (6)<span class="price">6.50</span></div>
      <div class="row">Steamed Shrimp Dumplings (4)<span class="price">6.50</span></div>
      <div class="row">Siu Mai Dumplings (4)<span class="price">6.50</span></div>
      <div class="row">Vegetable Dumplings (6)<span class="price">6.50</span></div>
      <div class="row">Three Kinds of Dumplings (</div>
      <div class="row">Pork, Vegetable, and Shrimp)<span class="price">6.95</span></div>
      <div class="row">Boneless Ribs<span class="price">7.95</span></div>
      <div class="row">Bacon Shrimp Rolls (6)<span class="price">8.50</span></div>
      <div class="row">Barbecued Spare Ribs (4) 9.95 (8)<span class="price">15.95</span></div>
      <div class="row">Pu Pu Platter (For 2)<span class="price">16.95</span></div>
      <div class="row note">Shrimp Toast, BBQ Spare Ribs,</div>
      <div class="row note">Beef Sticks, Shrimp Rolls, Siu Mai</div>
      <div class="row note">Dumplings, and Fried Dumplings</div>
    </div>

    <h2 class="block heading" style="top:874px;left:-30px"><span>Beef</span></h2>
    <div class="list" style="top:922px">
      <div class="row">Beef With Broccoli<span class="price">14.95</span></div>
      <div class="row">Beef With Snow Peas<span class="price">14.95</span></div>
      <div class="row">Pepper Steak With Onions<span class="price">14.95</span></div>
      <div class="row">Sauteed Shredded Hot Beef<span class="price">14.95</span></div>
      <div class="row">Beef With Mixed Vegetables<span class="price">14.95</span></div>
      <div class="row">&nbsp;Beef in Garlic Sauce<span class="price">14.95</span></div>
      <div class="row">Beef With Scallions<span class="price">14.95</span></div>
      <div class="row">Beef With Asparagus<span class="price">14.95</span></div>
    </div>
  </div>
</section>

<section class="panel panel--middle">
  <div class="panel__inner">
    <span class="corner corner--tl" role="img" aria-label="corner flourish"></span>
    <span class="corner corner--tr" role="img" aria-label="corner flourish"></span>
    <span class="corner corner--bl" role="img" aria-label="corner flourish"></span>
    <span class="corner corner--br" role="img" aria-label="corner flourish"></span>

    <h1 class="brand"><span class="brand__the">The</span><span class="brand__name">Jade Hall</span></h1>

    <h2 class="block heading" style="top:292px"><span>Chicken</span></h2>
    <div class="list" style="top:342px">
      <div class="row">Moo Shu Chicken<span class="price">13.50</span></div>
      <div class="row">Chicken With Broccoli<span class="price">13.50</span></div>
      <div class="row">Chicken With Mixed Vegetables<span class="price">13.50</span></div>
      <div class="row">Chicken With Cashew Nuts<span class="price">13.50</span></div>
      <div class="row">Kung Po Chicken With Peanuts<span class="price">13.50</span></div>
      <div class="row">Chicken in Garlic Sauce<span class="price">13.50</span></div>
      <div class="row">Chicken With String Beans<span class="price">13.50</span></div>
      <div class="row">Sweet &amp; Sour Chicken<span class="price">13.50</span></div>
      <div class="row">Chicken With Eggplant<span class="price">13.95</span></div>
      <div class="row">Hunan Chicken With Black Bean Sauce<span class="price">13.95</span></div>
      <div class="row">Chicken With Snow Peas<span class="price">13.95</span></div>
      <div class="row">Chicken With Asparagus<span class="price">13.95</span></div>
      <div class="row">Peppercorn Chicken<span class="price">13.95</span></div>
    </div>

    <h2 class="block heading" style="top:604px"><span>Pork</span></h2>
    <div class="list" style="top:648px">
      <div class="row">Sweet &amp; Sour Pork<span class="price">12.95</span></div>
      <div class="row">Pork in Garlic Sauce<span class="price">12.95</span></div>
      <div class="row">Sliced Pork With Mixed Vegetables<span class="price">12.95</span></div>
      <div class="row">Sliced Pork With String Beans<span class="price">12.95</span></div>
      <div class="row">Moo Shu Pork 12.95<span class="price">13.95</span></div>
    </div>

    <h2 class="block heading" style="top:762px"><span>Fish</span></h2>
    <div class="fish" style="top:810px">
      <div class="fish__name">Whole Fish<span class="fish__mp">Market Price</span></div>
      <div class="fish__desc">Steamed, Crispy, Hunan Style</div>
    </div>
    <div class="fish" style="top:861px">
      <div class="fish__name">Flounder Dragon Boat<span class="fish__mp">Market Price</span></div>
      <div class="fish__desc">Sliced Filet of Flounder Sautéed With Mixed Vegetables in a Delicate Ginger S callion Sauce Served Over a Crispy Fishbone</div>
    </div>
    <div class="fish" style="top:947px">
      <div class="fish__name">Heavenly Fish<span class="fish__mp">Market Price</span></div>
      <div class="fish__desc">Steamed Chilean Sea Bass Steak With a Choice of Ginger Scallion Sauce or Black Bean Sauce</div>
    </div>
    <div class="fish" style="top:1033px">
      <div class="fish__name">Crispy Chilean Sea Bass<span class="fish__mp">Market Price</span></div>
      <div class="fish__desc">Served With Fresh Scallions</div>
    </div>

    <p class="address">Space for Address and other information</p>
  </div>
</section>

<section class="panel panel--right">
  <div class="panel__inner">
    <span class="corner corner--tl" role="img" aria-label="corner flourish"></span>
    <span class="corner corner--tr" role="img" aria-label="corner flourish"></span>
    <span class="corner corner--bl" role="img" aria-label="corner flourish"></span>
    <span class="corner corner--br" role="img" aria-label="corner flourish"></span>

    <h2 class="block heading" style="top:64px"><span>Sea Food</span></h2>
    <div class="list" style="top:110px">
      <div class="row">Moo Shu Shrimp (With 4 Pancakes)<span class="price">15.95</span></div>
      <div class="row">Shrimp With Broccoli<span class="price">17.50</span></div>
      <div class="row">Shrimp With Mixed Vegetables<span class="price">17.50</span></div>
      <div class="row">Shrimp in Lobster Sauce<span class="price">17.50</span></div>
      <div class="row">Shrimp in Black Bean Sauce<span class="price">17.50</span></div>
      <div class="row">Shrimp in Garlic Sauce<span class="price">17.50</span></div>
      <div class="row">Kung Po Shrimp With Peanuts<span class="price">17.50</span></div>
      <div class="row">Shrimp With Asparagus<span class="price">17.95</span></div>
      <div class="row">Scallops in Garlic Sauce<span class="price">17.95</span></div>
      <div class="row">Scallops With Mixed Vegetables<span class="price">17.95</span></div>
    </div>

    <h2 class="block heading" style="top:320px"><span>House Specialties</span></h2>

    <div class="special" style="top:365px">
      <div class="special__name">Basil Chicken<span class="price">15.50</span></div>
      <div class="special__desc">Chunks of Dark Meat Chicken Sautéed in a Deli-cious Basil Sauce With Fresh Ginger and Garlic.</div>
    </div>
    <div class="special" style="top:441px">
      <div class="special__name">Sesame Chicken<span class="price">15.50</span></div>
      <div class="special__desc">Crispy Chunks of Chicken Sautéed in a Sweet Brown Sauce With a Shower of Sesame Seeds.</div>
    </div>
    <div class="special" style="top:518px">
      <div class="special__name">General Tso’s Chicken<span class="price">15.50</span></div>
      <div class="special__desc">Crispy Chicken Sautéed in Our Tangy General Tso’s Sauce.</div>
    </div>
    <div class="special" style="top:594px">
      <div class="special__name">Tangerine Chicken<span class="price">15.50</span></div>
      <div class="special__desc">Crispy Chunks of Chicken Sautéed in a Tangerine Flavored Spicy Sauce.</div>
    </div>
    <div class="special" style="top:670px">
      <div class="special__name">Imperial Chicken<span class="price">15.50</span></div>
      <div class="special__desc">Chunks of Chicken, Dry Sautéed With Three Kinds of Hot Peppers.</div>
    </div>
    <div class="special" style="top:746px">
      <div class="special__name">Peking Pork Chop<span class="price">16.95</span></div>
      <div class="special__desc">Marinated Slices of Pork Chop Lightly Fried, Then Sautéed With Our Special Tangy Peking Sauce.</div>
    </div>
    <div class="special" style="top:822px">
      <div class="special__name">&nbsp;Mandarin Pork Chop<span class="price">16.95</span></div>
      <div class="special__desc">Crispy Slices of Pork Chop Marinated With Our Chef’s Special Sauce Then Sautéed With Fresh Shredded Scallions.</div>
    </div>
    <div class="special" style="top:906px">
      <div class="special__name">Golden Orange Chicken<span class="price">16.95</span></div>
      <div class="special__desc">Crispy White Meat Chicken Sautéed With Fresh Fruit in a Sweet Golden Orange Sauce With Cashew Nuts.</div>
    </div>

    <span class="divider" role="img" aria-label="ornamental divider"></span>
    <p class="footnote">Hot &amp; Spicy<br>We Can Alter the Spiciness Accorsing to Yor Taste<br>Crispy Noodles Only Come With Soup or Show Mein<br>Additional Sauce on the Side- Extra Charge $2.00</p>
    <p class="call">Call Us ---------------</p>
  </div>
</section>

</body>
</html>
```